Customer Journey Graphic

I want to graphic to describe a marketing framework I am teaching a course on

It a framework for growing a business
The idea is we
get customers to "take a Journey" through 7 steps
to deliver value to them

There are 4 major concepts that impact this journey - Game Plan, Business Model, "Inside out thinking' and Unique Competitive advantage
These concepts can make the journey faster, get more people to take it or make it more valuable

The stages are

- Target
- attract
- nurture
- convert
- maximise
- loyalty
- reactivation

I want to uses this framework as an overall;; 'explainer' fro my idea ,so it must looks very professional, and work well in presentations

I have included a rought 'sketch; of my thinking as an attachment

Business Owners

Business

Serif

• clear, get acroess the idea of a Journye over times, teh idea you can improve your results throught applying concpets of ' business model', "inside out thinking: , unique competitive advantage and game plane

```html
<!DOCTYPE html>
<html lang="en">
<head>
<meta charset="utf-8">
<title>Customer Journey Framework</title>
<link href="https://fonts.googleapis.com/css2?family=Oswald:wght@600&display=swap" rel="stylesheet">
<style>
  :root {
    --bg: #ffffff;
    --ink: #000000;
    --icon: #ffffff;
    --inside-out: #46b549;
    --advantage: #5ec6d4;
    --business-model: #f58720;
    --gameplan: #f16b64;
    --label: #ffffff;
  }
  html, body {
    margin: 0;
    padding: 0;
    width: 1200px;
    height: 900px;
    overflow: hidden;
    background: var(--bg);
  }
  .framework {
    position: relative;
    width: 1200px;
    height: 900px;
  }
  .concept-ring {
    position: absolute;
    left: 0;
    top: 0;
    width: 1200px;
    height: 900px;
  }
  .concept-segment {
    stroke: var(--bg);
    stroke-width: 8;
    stroke-linejoin: miter;
  }
  .concept-segment.inside-out { fill: var(--inside-out); }
  .concept-segment.advantage { fill: var(--advantage); }
  .concept-segment.business-model { fill: var(--business-model); }
  .concept-segment.gameplan { fill: var(--gameplan); }
  .concept-label {
    font-family: "Oswald", "Arial Narrow", sans-serif;
    font-weight: 600;
    font-size: 31px;
    letter-spacing: 1px;
    fill: var(--label);
  }
  .journey-stage {
    position: absolute;
    top: 399px;
    width: 105px;
    height: 105px;
    margin-left: -52.5px;
    background: var(--ink);
    border-radius: 11px;
  }
  .journey-stage svg {
    display: block;
    width: 105px;
    height: 105px;
  }
  .stage-target { left: 84px; }
  .stage-attract { left: 211px; }
  .stage-nurture { left: 475px; }
  .stage-convert { left: 601px; }
  .stage-maximise { left: 727px; }
  .stage-loyalty { left: 996px; }
  .stage-reactivation { left: 1123px; }
  .glyph-line { fill: none; stroke: var(--icon); }
  .glyph-fill { fill: var(--icon); }
  .glyph-cut { fill: var(--ink); stroke: var(--ink); }
</style>
</head>
<body>
<main class="framework">

  <svg class="concept-ring" viewBox="0 0 1200 900" aria-label="Four concepts: Inside Out Thinking, Unique Advantage, Business Model, Gameplan">
    <defs>
      <path id="arc-inside-out" d="M348.9,383.7 A260,260 0 0 1 622.7,192"/>
      <path id="arc-advantage" d="M667.3,199.9 A260,260 0 0 1 859,473.7"/>
      <path id="arc-business-model" d="M577.3,710 A260,260 0 0 0 851.1,518.3"/>
      <path id="arc-gameplan" d="M341,428.3 A260,260 0 0 0 532.7,702.1"/>
    </defs>

    <path class="concept-segment inside-out" d="M270.5,410.5 A332,332 0 0 1 640.5,121.5 L658.5,197.7 L622.9,264.4 A188,188 0 0 0 413.4,428.1 L346.7,392.5 Z"/>
    <path class="concept-segment advantage" d="M640.5,121.5 A332,332 0 0 1 929.5,491.5 L853.3,509.5 L786.6,473.9 A188,188 0 0 0 622.9,264.4 L658.5,197.7 Z"/>
    <path class="concept-segment business-model" d="M929.5,491.5 A332,332 0 0 1 559.5,780.5 L541.5,704.3 L577.1,637.6 A188,188 0 0 0 786.6,473.9 L853.3,509.5 Z"/>
    <path class="concept-segment gameplan" d="M559.5,780.5 A332,332 0 0 1 270.5,410.5 L346.7,392.5 L413.4,428.1 A188,188 0 0 0 577.1,637.6 L541.5,704.3 Z"/>

    <text class="concept-label" dominant-baseline="central"><textPath href="#arc-inside-out" startOffset="50%" text-anchor="middle">Inside Out Thinking</textPath></text>
    <text class="concept-label" dominant-baseline="central"><textPath href="#arc-advantage" startOffset="50%" text-anchor="middle">Unique Advantage</textPath></text>
    <text class="concept-label" dominant-baseline="central"><textPath href="#arc-business-model" startOffset="50%" text-anchor="middle">Business Model</textPath></text>
    <text class="concept-label" dominant-baseline="central"><textPath href="#arc-gameplan" startOffset="50%" text-anchor="middle">Gameplan</textPath></text>
  </svg>

  <div class="journey-stage stage-target" aria-label="Target">
    <svg viewBox="0 0 100 100">
      <circle class="glyph-line" cx="50" cy="52" r="34" stroke-width="6"/>
      <circle class="glyph-line" cx="50" cy="52" r="22" stroke-width="6"/>
      <circle class="glyph-fill" cx="50" cy="52" r="9"/>
    </svg>
  </div>

  <div class="journey-stage stage-attract" aria-label="Attract">
    <svg viewBox="0 0 100 100">
      <g transform="rotate(-45 50 50)">
        <path class="glyph-line" d="M31,20 V52 a19,19 0 0 0 38,0 V20" stroke-width="15"/>
        <line class="glyph-cut" x1="20" y1="31" x2="80" y2="31" stroke-width="3"/>
      </g>
    </svg>
  </div>

  <div class="journey-stage stage-nurture" aria-label="Nurture">
    <svg viewBox="0 0 100 100">
      <path class="glyph-line" d="M50,64 V34" stroke-width="5"/>
      <path class="glyph-fill" d="M50,42 C36,42 28,34 28,22 C42,22 50,30 50,42 Z"/>
      <path class="glyph-fill" d="M50,48 C64,48 74,40 74,28 C60,28 50,36 50,48 Z"/>
      <path class="glyph-fill" d="M12,70 Q26,64 40,68 L58,68 Q64,70 58,74 L44,74 L60,76 L82,64 Q90,62 88,70 L66,84 Q58,88 48,86 L12,82 Z"/>
    </svg>
  </div>

  <div class="journey-stage stage-convert" aria-label="Convert">
    <svg viewBox="0 0 100 100">
      <circle class="glyph-line" cx="50" cy="50" r="33" stroke-width="13" stroke-dasharray="12.96 12.96"/>
      <circle class="glyph-line" cx="50" cy="50" r="22" stroke-width="16"/>
    </svg>
  </div>

  <div class="journey-stage stage-maximise" aria-label="Maximise">
    <svg viewBox="0 0 100 100">
      <rect class="glyph-fill" x="18" y="72" width="12" height="12"/>
      <rect class="glyph-fill" x="36" y="62" width="12" height="22"/>
      <rect class="glyph-fill" x="54" y="50" width="12" height="34"/>
      <rect class="glyph-fill" x="72" y="38" width="12" height="46"/>
      <path class="glyph-line" d="M18,58 L72,22" stroke-width="5"/>
      <polygon class="glyph-fill" points="82,14 62,18 76,34"/>
    </svg>
  </div>

  <div class="journey-stage stage-loyalty" aria-label="Loyalty">
    <svg viewBox="0 0 100 100">
      <circle class="glyph-line" cx="50" cy="50" r="16" stroke-width="8" stroke-dasharray="8.38 8.38"/>
      <circle class="glyph-line" cx="50" cy="50" r="10" stroke-width="8"/>
      <path class="glyph-line" d="M20,42 A31,31 0 0 1 68,24" stroke-width="5"/>
      <polygon class="glyph-fill" points="74,16 76,32 62,28"/>
      <path class="glyph-line" d="M80,58 A31,31 0 0 1 32,76" stroke-width="5"/>
      <polygon class="glyph-fill" points="26,84 24,68 38,72"/>
    </svg>
  </div>

  <div class="journey-stage stage-reactivation" aria-label="Reactivation">
    <svg viewBox="0 0 100 100">
      <path class="glyph-line" d="M30,28 A30,30 0 1 1 22,62" stroke-width="9"/>
      <polygon class="glyph-fill" points="16,18 40,20 20,42"/>
    </svg>
  </div>

</main>
</body>
</html>
```